Modern, Bright Bubble Bath Label

We need a label design for a private label bubble bath we will begin selling.

We will have 8 different scents of bubble bath. Each has a color associated with it as follows: Napa Valley Grape (Purple), Mixed Berry (Blue), Bartlett Pear (Green), Sweet Pineapple (Yellow), Juicy Peach (Orange), Red Raspberry (Red), Creamy Coconut (Brown or White), Kiwi Watermelon (Pink). So what we want is 8 different bottle labels. The labels CAN be different, but they will likely be the same label, just with a different color and different text (scent name).

Labels should be bright, fun, modern, and clean. The main color should be what is listed above, but other colors can be incorporated, as can be seen in the attachments.

Label should be between 2.5" and 3.5" tall, and 7.25" wide. This will be applied to an 8oz boston round, plastic, transparent bottle with a black cap.

For reference, I love The Fern Parlor packaging designs.

Target Market(s)

Women

Industry/Entity Type

Hair And Beauty

Logo Text

Amber Cove

Font styles to use
Serif
Sans Serif

Requirements
Must have
• -Company Logo: 'Amber Cove', which will need to be designed by the winning designer. You can simply put 'Amber Cove' in the label for now as a place holder.
• -Text 'Glimmering Foam Bath'
• -Name of Scent
• -Packaging that is brightly colored and associated with the scent as mentioned in the product description.
• Should be in format that can be edited in Adobe Photoshop. We will add additional text and details (ingredients, description, etc.) in Photoshop once we choose the winning design
Nice to have
• Picture or graphic of associated fruit

```html
<!DOCTYPE html>
<html lang="en">
<head>
<meta charset="utf-8">
<title>Amber Cove – Red Raspberry Glimmering Foam Bath Label</title>
<link rel="stylesheet" href="https://fonts.googleapis.com/css2?family=Poiret+One&family=Fredoka:wght@500&family=Sniglet&display=swap">
<style>
  :root {
    --paper: #ffffff;
    --label-black: #050607;
    --berry-red: #e8213a;
    --berry-deep: #c81a30;
    --berry-light: #f4516a;
    --text-white: #ffffff;
  }
  html, body {
    margin: 0;
    padding: 0;
    width: 1200px;
    height: 2484px;
    overflow: hidden;
    background: var(--paper);
  }
  .label {
    position: relative;
    width: 1200px;
    height: 2484px;
    background: var(--paper);
  }
  .label-art {
    position: absolute;
    inset: 0;
    width: 1200px;
    height: 2484px;
  }
  .brand-name {
    position: absolute;
    left: 124px;
    width: 1000px;
    top: 752px;
    margin: 0;
    text-align: center;
    white-space: nowrap;
    font-family: "Poiret One", sans-serif;
    font-weight: 400;
    font-size: 112px;
    line-height: 1;
    color: var(--text-white);
    letter-spacing: 1px;
  }
  .scent-name {
    position: absolute;
    left: 206px;
    width: 800px;
    top: 1068px;
    margin: 0;
    text-align: center;
    white-space: nowrap;
    font-family: "Fredoka", sans-serif;
    font-weight: 500;
    font-size: 132px;
    line-height: 140px;
    color: var(--berry-red);
    letter-spacing: 5px;
  }
  .product-type {
    position: absolute;
    left: 173px;
    width: 800px;
    top: 1490px;
    margin: 0;
    text-align: center;
    white-space: nowrap;
    font-family: "Sniglet", sans-serif;
    font-size: 68px;
    line-height: 1;
    color: var(--text-white);
  }
</style>
</head>
<body>
<main class="label">
  <svg class="label-art" viewBox="0 0 500 1035" width="1200" height="2484">
    <defs>
      <radialGradient id="fruit-fill" cx="0.4" cy="0.45" r="0.7">
        <stop offset="0" stop-color="#f25470"/>
        <stop offset="1" stop-color="#d81c36"/>
      </radialGradient>
      <linearGradient id="bubble-area-fill" x1="0" y1="0" x2="0" y2="1">
        <stop offset="0" stop-color="var(--berry-red)" stop-opacity="0"/>
        <stop offset="0.45" stop-color="var(--berry-red)" stop-opacity="0.55"/>
        <stop offset="1" stop-color="var(--berry-red)"/>
      </linearGradient>
      <clipPath id="label-body-clip">
        <path d="M65,905 L65,300 Q65,240 105,240 L105,130 Q105,40 250,40 Q395,40 395,130 L395,240 Q440,240 440,300 L440,905 Q440,965 380,965 L125,965 Q65,965 65,905 Z"/>
      </clipPath>
    </defs>

    <path class="label-body" fill="var(--label-black)"
          d="M65,905 L65,300 Q65,240 105,240 L105,130 Q105,40 250,40 Q395,40 395,130 L395,240 Q440,240 440,300 L440,905 Q440,965 380,965 L125,965 Q65,965 65,905 Z"/>

    <ellipse class="fruit-illustration" role="img" aria-label="Illustration of a red raspberry with green leaves"
             cx="255" cy="175" rx="118" ry="128" fill="url(#fruit-fill)"/>

    <rect class="bubble-illustration" role="img" aria-label="Illustration of rising red bubbles with white sparkles"
          x="65" y="680" width="375" height="285"
          clip-path="url(#label-body-clip)" fill="url(#bubble-area-fill)"/>
  </svg>

  <h1 class="brand-name">Amber Cove</h1>
  <h2 class="scent-name">RED<br>RASPBERRY</h2>
  <p class="product-type">glimmering foam bath</p>
</main>
</body>
</html>
```